Wordpress Design for my Consulting Company

We want a WordPress site created for our new business. We have created a mock-up of the content we want on the site at https://marcobellweather.example.com/website-5

We are not attached to any of the pictures and just put stock stuff from bloq's editor, which we don't have rights to use outside of bloq.

We are NOT looking to just port this site to WordPress, we are looking for some creative ways to display the content in a more professional artistic sense.

I have included several logo files and a text file with the colors and Fonts used in the logo. We are not looking to change the logo or the colors used in the logo.

The Schedule appointment links to a page that embeds a bookslot.example calendar. https://bookslot.example.com/marco-bellweather/trailguide

The final website domain will be venturelanterns.example

Venture lanterns is a consulting company that works directly with the business owners and leaders of small businesses between 50-200 employees. We help companies make sure they have the right technology to meet their strategic goals. We are the anti-"Computer Guy" and we focus on business outcomes NOT cool technology gadgets.

The final design should communicate business growth and success.

Target Market(s)

Business Owners of companies with 50-200 employees

Coding

Coded - Design and coding required

Number of Pages Required

1 page

Font styles to use
Serif
Other font styles liked:
• Trajan Pro Bold, Open Sans

Requirements
Must have
• Should focus on consulting rather than technology.
• Should show the customer as the hero and we are just their guide.
• Must use the logo provided and the colors and fonts in the text file provided. Any other colors and fonts must be complementary.
• The design should scale for all devices computer, iPad, or phone
Should not have
• Should not focus on technology, we are the anti-"Computer Guy" and we focus on business outcomes NOT cool technology gadgets.

```html
<!DOCTYPE html>
<html lang="en">
<head>
<meta charset="utf-8">
<title>Venture Lanterns — Contact</title>
<link href="https://fonts.googleapis.com/css2?family=Poppins:wght@500;600&family=Rubik:wght@400;500&display=swap" rel="stylesheet">
<style>
  :root {
    --ink: #3a3a3a;
    --ink-soft: #555555;
    --muted: #8a8a8a;
    --rule: #d9d9d9;
    --accent: #d9884f;
    --paper: #ffffff;
    --hero-a: #f4f1ee;
    --hero-b: #faf8f6;
  }
  * { box-sizing: border-box; margin: 0; padding: 0; }
  html, body { width: 1200px; height: 608px; overflow: hidden; background: var(--paper); }
  body { position: relative; font-family: "Rubik", sans-serif; color: var(--ink); }

  .side-rail {
    position: absolute; left: 0; top: 0; width: 64px; height: 608px;
    background: var(--paper); box-shadow: 2px 0 6px rgba(0,0,0,0.05); z-index: 2;
  }
  .menu-toggle { position: absolute; left: 23px; top: 21px; width: 17px; }
  .menu-toggle span { display: block; height: 2px; background: var(--ink); margin-bottom: 3.5px; }
  .rail-mark {
    position: absolute; left: 32px; top: 262px;
    transform: translate(-50%, -50%) rotate(-90deg);
    font-size: 8px; letter-spacing: 0.3px; white-space: nowrap; color: var(--ink);
  }
  .rail-line { position: absolute; left: 31px; top: 325px; width: 1px; height: 48px; background: var(--rule); }
  .rail-line::before { content: ""; position: absolute; left: 0; top: 0; width: 1px; height: 24px; background: var(--ink); }

  .contact-hero {
    position: absolute; left: 64px; top: 0; width: 1136px; height: 232px;
    background: linear-gradient(100deg, var(--hero-a) 0%, var(--hero-b) 45%, #f2eeea 80%, #f6f3f0 100%);
  }
  .message-rule { position: absolute; left: 378px; top: 84px; width: 703px; height: 1px; background: var(--rule); }
  .btn {
    position: absolute; display: flex; align-items: center; justify-content: center;
    border-radius: 20px; font-family: "Poppins", sans-serif; font-weight: 500; background: transparent;
  }
  .btn-send { left: 378px; top: 102px; width: 73px; height: 37px; border: 1px solid var(--accent); font-size: 11.5px; color: var(--ink); }

  .newsletter { position: absolute; left: 98px; top: 300px; width: 336px; }
  .newsletter-field {
    font-size: 11.5px; color: var(--muted); padding-top: 4px;
    height: 30px; border-bottom: 1px solid var(--ink-soft);
  }
  .btn-subscribe { left: 0; top: 42px; width: 98px; height: 38px; border: 1px solid var(--ink-soft); font-size: 11.5px; color: var(--ink-soft); font-weight: 600; }
  .newsletter-note { position: absolute; top: 113px; font-size: 11px; line-height: 21px; color: var(--ink-soft); width: 340px; }

  .say-hello { position: absolute; left: 612px; top: 290px; width: 340px; }
  .say-hello h2 { font-family: "Poppins", sans-serif; font-weight: 600; font-size: 13.5px; color: var(--ink-soft); margin-bottom: 18px; }
  .say-hello p { font-size: 11.8px; line-height: 18.5px; color: var(--ink-soft); margin-bottom: 8.5px; }

  .social-links { position: absolute; left: 612px; top: 461px; display: flex; gap: 8px; }
  .social-links span { width: 34px; height: 34px; border: 1px solid var(--ink-soft); border-radius: 50%; }

  .footer-rule { position: absolute; left: 98px; top: 545px; width: 1004px; height: 1px; background: var(--rule); }
  .footer-legal { position: absolute; left: 98px; top: 573px; font-size: 10.5px; color: var(--muted); }
  .footer-legal a { color: var(--muted); }
  .footer-rights { position: absolute; right: 98px; top: 573px; font-size: 10.5px; color: var(--muted); }

  .to-top { position: absolute; left: 1133px; top: 541px; width: 42px; height: 42px; }
</style>
</head>
<body>
  <aside class="side-rail">
    <div class="menu-toggle"><span></span><span></span><span></span></div>
    <div class="rail-mark">© 2018, VENTURE LANTERNS</div>
    <div class="rail-line"></div>
  </aside>

  <section class="contact-hero" role="img" aria-label="Softly faded photo of colleagues meeting at a bright office desk">
    <div class="message-rule"></div>
    <div class="btn btn-send">Send</div>
  </section>

  <div class="newsletter">
    <div class="newsletter-field">Enter your email</div>
    <div class="btn btn-subscribe">Subscribe</div>
    <p class="newsletter-note">Be the first to find out about exclusive deals, the latest Lookbooks, and top trends.</p>
  </div>

  <div class="say-hello">
    <h2>Say Hello</h2>
    <p>Phone: +1-555-014-2370</p>
    <p>Email: mbellweather@venturelanterns.example</p>
    <p>Address: 4120 Harbor Crest Parkway, Suite 310 Lakeview, TX 77001</p>
  </div>

  <div class="social-links" aria-label="Social profiles">
    <span aria-label="Social profile 1"></span>
    <span aria-label="Social profile 2"></span>
    <span aria-label="Social profile 3"></span>
    <span aria-label="Social profile 4"></span>
  </div>

  <div class="footer-rule"></div>
  <div class="footer-legal">© 2018, Venture Lanterns | <a href="#">Privacy Policy</a> | <a href="#">Sitemap</a></div>
  <div class="footer-rights">All Rights Reserved.</div>

  <svg class="to-top" viewBox="0 0 42 42" aria-label="Back to top">
    <circle cx="21" cy="21" r="20.5" fill="none" stroke="#d9884f" stroke-width="1"/>
    <path d="M21 29 V13 M16 18 L21 13 L26 18" fill="none" stroke="#d9884f" stroke-width="1"/>
  </svg>
</body>
</html>
```